Electrical panel service sticker w Bucket truck & Logo

We have a rather plain sticker we put on lighting panels to remind customers who to call for service. We want to redesign them with brushed aluminum background. We want a remake of the sticker with the outline of a bucket truck. You'll need to find or draw the outling of a bucket truck maybe with the boom up slightly as we will get these stickers die cut.

We want LOGO with Ph.# and Email.
Electrical * Lighting * Sign Service

Target Market(s)

Commercial property managers

Industry/Entity Type

Property Management

Requirements
Must have
• Bucket Truck Outline

```html
<!DOCTYPE html>
<html lang="en">
<head>
<meta charset="utf-8">
<title>Brightline Fixture Service – Panel Service Sticker</title>
<link rel="stylesheet" href="https://fonts.googleapis.com/css2?family=Rubik:wght@800&family=Roboto:wght@500;700&display=swap">
<style>
  :root {
    --metal-light: #f4f5f6;
    --metal-mid: #d6d8db;
    --metal-dark: #a9adb2;
    --frame-navy: #13304f;
    --brand-red: #e0403a;
    --phone-navy: #0f2a46;
    --ink: #111318;
    --rule: #3a3a3a;
    --art-tone: #1a1a1a;
  }
  * { margin: 0; padding: 0; box-sizing: border-box; }
  html, body { width: 1200px; height: 900px; overflow: hidden; background: #ffffff; }
  .sticker {
    position: relative;
    width: 1200px;
    height: 900px;
    border-radius: 28px;
    overflow: hidden;
    background:
      repeating-linear-gradient(0deg, rgba(255,255,255,0.18) 0 1px, rgba(0,0,0,0.03) 1px 3px),
      radial-gradient(ellipse 55% 70% at 50% 45%, rgba(255,255,255,0.95), rgba(255,255,255,0) 70%),
      linear-gradient(100deg, var(--metal-dark) 0%, var(--metal-light) 18%, var(--metal-mid) 32%, var(--metal-light) 50%, var(--metal-mid) 68%, var(--metal-light) 82%, var(--metal-dark) 100%);
  }
  .sticker__frame { position: absolute; inset: 0; }
  .truck-art {
    position: absolute;
    left: 438px; top: 62px;
    width: 343px; height: 256px;
    background: var(--art-tone);
    border-radius: 6px;
  }
  .rule { position: absolute; height: 3px; background: var(--rule); }
  .brand {
    position: absolute; left: 0; right: 0;
    text-align: center;
    font-family: "Rubik", sans-serif;
    font-weight: 800;
    color: var(--brand-red);
    text-transform: uppercase;
    line-height: 1;
  }
  .brand--line1 { top: 330px; font-size: 78px; }
  .brand--line2 { top: 418px; font-size: 78px; }
  .brand--line3 { top: 510px; font-size: 38px; }
  .phone {
    position: absolute; left: 0; right: 0; top: 590px;
    text-align: center;
    font-family: "Roboto", sans-serif; font-weight: 700;
    font-size: 104px; line-height: 1;
    color: var(--phone-navy);
  }
  .email {
    position: absolute; left: 0; right: 0; top: 718px;
    text-align: center;
    font-family: "Roboto", sans-serif; font-weight: 500;
    font-size: 44px; line-height: 1;
    color: var(--ink);
  }
  .services {
    position: absolute; left: 0; right: 0; top: 782px;
    text-align: center;
    font-family: "Roboto", sans-serif; font-weight: 500;
    font-size: 36px; line-height: 1;
    color: var(--ink);
  }
</style>
</head>
<body>
  <div class="sticker">
    <svg class="sticker__frame" width="1200" height="900" viewBox="0 0 1200 900" aria-hidden="true">
      <path d="M78 38 H1122 A22 22 0 0 0 1144 60 V840 A22 22 0 0 0 1122 862 H78 A22 22 0 0 0 56 840 V60 A22 22 0 0 0 78 38 Z"
            fill="none" stroke="var(--frame-navy)" stroke-width="6"/>
      <g fill="#c9ccd0" stroke="#8a8e94" stroke-width="3">
        <circle cx="42" cy="44" r="15"/>
        <circle cx="1158" cy="44" r="15"/>
        <circle cx="42" cy="858" r="15"/>
        <circle cx="1158" cy="858" r="15"/>
      </g>
      <g fill="#eef0f2">
        <circle cx="42" cy="44" r="7"/>
        <circle cx="1158" cy="44" r="7"/>
        <circle cx="42" cy="858" r="7"/>
        <circle cx="1158" cy="858" r="7"/>
      </g>
    </svg>

    <div class="truck-art" role="img" aria-label="Outline illustration of a bucket truck with its boom raised"></div>

    <div class="rule" style="left:258px; top:290px; width:148px;"></div>
    <div class="rule" style="left:794px; top:290px; width:148px;"></div>
    <div class="rule" style="left:250px; top:370px; width:110px;"></div>
    <div class="rule" style="left:850px; top:370px; width:110px;"></div>
    <div class="rule" style="left:250px; top:536px; width:140px;"></div>
    <div class="rule" style="left:812px; top:536px; width:140px;"></div>

    <div class="brand brand--line1">Brightline</div>
    <div class="brand brand--line2">Fixture Service</div>
    <div class="brand brand--line3">Incorporated</div>

    <div class="phone">877-555-0148</div>
    <div class="email">SERVICE@BRIGHTLINEFIXTURE.COM</div>
    <div class="services">ELECTRICAL • LIGHTING • SIGN SERVICE</div>
  </div>
</body>
</html>
```